New Website for QWRB Holdings (Property Leasing Company in New Haven)

Design a fully functioning website for a real estate property leasing company. The company has a few properties in New Haven, CT and would like to provide an option for its tenants to pay their rent online. The company should have the ability to generate unique account log in username and password for its tenants so they can make online payments through ACH the website. (The ACH processing part will be coordinated with the bank).

Please take a look at all the pictures I uploaded of New Haven especially the area around Marlow College, you will find that the general style is Gothic and charming.

Also please make use of the pictures of the two properties I have attached to the description.

Please keep Holdings page, Contact Us Page , About Us Page, and please add a page entitled "Tenants".

On the Holdings page I would like to see on the left hand side an interactive map of new haven (Please see a map attached), split by New Haven's neighbourhoods, and showing my properties as pins of sort on the map (I can send you the addresses of the properties upon request). On the same page on the right side I want to see a drop down menu that includes list of New Haven Neighbourhoods. When a neighbourhood is selected you can see in the space underneath the drop-down menu the properties we have in that neighbourhood in large thumbnail format. Also on the map you can see the pins corresponding to those properties change colour. A user can either click on the pin or on the thumbnails to have view more pictures of the property and some details in text.

The tenants page should prompt a login to access- I like your idea of having the company name in two colours, one for QWRB and another for Holdings.Please let me know if you have any questions along the way

-------------------------------------------------------------------------------
Property Descriptions for Holdings Page
The Larch Lodge,

Neighbourhood: Westville
Name: Silas Brennaway House
Building Style: Queen Anne Style
Address: 418 Pellwin Road, New Haven, CT 06515
Number of Units: 3
Unit Names: Unit 1, Unit 2, Unit 3

Property Description

This Westiville home was built in 1897, historically known as The Silas Brennaway House, it is an example of the Queen Anne style. The large carriage house is still intact and sits in the lovely, expansive back garden! An outstanding architectural feature of the house is the turret, giving the home prominence on Pellwin Road. This well maintained home has renovated kitchens in all units, the first floor has granite and red oak cabinetry. New baths and central air in all apartments. All newer mechanicals for each unit, all natural gas. The entire house has replacement windows. The new back deck overlooks the back garden and carriage house. The front steps and porch have also been rebuilt. Roof has 30 year architectural singles and approximately 15 years old, the chimney has just been lined.

Unit 1 Description:

2 Bedrooms, 6 rooms in total.
Amenities: Dishwasher, Central Air, Gas Heating, Porch

Unit 2 Description:

2 Bedrooms, 5 rooms in total.
Amenities: Dishwasher, Central Air, Gas Heating, Balcony

Unit 3 Description:

2 Bedrooms, 4 rooms in total.
Amenities: Dishwasher, Central Air, Gas Heating

The Fern Lodge:

Neighbourhood: East Rock
Name: 64 Birchmere
Building Style: Victorian
Address: 64 Birchmere Lane, New Haven, CT 06511
Number of Units: 2
Unit Names: Unit 1, and Unit 2

Property Description

East Rock incredibly charming newly renovated 2 family on quiet tree-lined block. Tenants are responsible for all utilities (gas heat, electricity and cable). Small pets are possible with landlord approval. Tenants has use of shared yard, laundry in the basement and on street parking only. Located steps away from gourmet markets & minutes to Downtown New Haven, Marlow & local hospitals. Fascinating backyard. This is a feel good house!

Unit 1 Description:

Area:
1100 soft, 3 Bedrooms, 5 rooms in total.
Amenities: In unit Washer and Dryer, Central Air, Gas Heating, Porch, Backyard

Unit 2 Description:

Area: 2,820 sqft
5 Bedrooms, 8 rooms in total.
Amenities: In unit Washer and Dryer, Dishwasher, Central Air, and Gas Heating

Target Market(s)

1-3 bedroom Renting Market around Marlow College and New Haven Community

Industry/Entity Type

Real Estate

Coding

Coded - Design and coding required

Number of Pages Required

4 page

Font styles to use
Other font styles liked:
• Helvetica

Colors
85cae6
cee9f5
d9d9d9
9d9d9d

Requirements
Must have
• Payment page with login (accounts can only be created by administrator)
• A page showcasing the properties (Professional photos to be uploaded shortly)
• A page for technical support, contact information and so forth
• Home page
Nice to have
• A professional, but stylish design. Not too colourful, something with pastel colours
Should not have
• A lot of colours, any pop-ups,

```html
<!DOCTYPE html>
<html lang="en">
<head>
<meta charset="utf-8">
<title>QWRB Holdings</title>
<link href="https://fonts.googleapis.com/css2?family=Open+Sans:wght@400;600;700&display=swap" rel="stylesheet">
<style>
:root{
  --blue:#85cae6;
  --blue-dark:#5fb4d8;
  --blue-pale:#cee9f5;
  --grey-light:#d9d9d9;
  --grey:#9d9d9d;
  --text:#555;
  --heading:#333;
  --footer:#2f2f2f;
  --footer-bottom:#252525;
  --page:#ffffff;
  --panel:#f4f4f4;
}
*{box-sizing:border-box;margin:0;padding:0}
html,body{width:1200px;height:2392px;overflow:hidden;background:var(--page);font-family:"Open Sans",Helvetica,Arial,sans-serif;color:var(--text)}
.page{position:relative;width:1200px;height:2392px;overflow:hidden}
.abs{position:absolute}

/* hero */
.hero{left:0;top:0;width:1200px;height:740px;background:linear-gradient(180deg,#6f93c4 0%,#9fb7d8 35%,#c9b6c6 55%,#7e8fa3 72%,#4a5b68 100%)}
.nav{left:0;top:0;width:1200px;height:80px;display:flex;align-items:center;padding:0 100px}
.brand{display:flex;align-items:center;gap:12px;color:#fff;font-size:30px;font-weight:600;line-height:1}
.brand-dot{width:48px;height:48px;border-radius:50%;border:2px solid #fff}
.menu{margin-left:auto;display:flex;gap:34px;align-items:center;list-style:none}
.menu li{color:#fff;font-size:13px;font-weight:600;letter-spacing:.5px}
.menu .login{border:2px solid #fff;padding:8px 16px}
.hero-title{left:0;top:380px;width:1200px;text-align:center;color:#fff;font-size:56px;font-weight:600;letter-spacing:3px}
.hero-btn{left:510px;top:494px;width:180px;height:40px;background:var(--blue);color:#fff;font-size:13px;font-weight:600;display:flex;align-items:center;justify-content:center;letter-spacing:.5px}
.slide-arrow{top:405px;width:34px;height:50px;background:rgba(0,0,0,.35);display:flex;align-items:center;justify-content:center}

/* search */
.search{left:100px;top:640px;width:1000px;height:160px;background:#fff;box-shadow:0 2px 8px rgba(0,0,0,.12);padding:26px 30px}
.field{height:36px;border:1px solid var(--grey-light);font-size:12px;color:var(--grey);display:flex;align-items:center;padding:0 12px}
.search-row{display:flex;gap:20px;margin-top:18px;align-items:flex-end}
.search-col{width:118px}
.search-col label{display:block;font-size:11px;color:var(--grey);margin-bottom:6px}
.search-btn{width:118px;height:36px;background:var(--blue);color:#fff;font-size:12px;font-weight:700;display:flex;align-items:center;justify-content:center;margin-left:auto}

/* main */
.h2{font-size:30px;font-weight:600;color:var(--heading)}
.h2 .accent{color:var(--blue)}
.para{font-size:13px;line-height:22px;color:var(--grey)}
.card{width:236px}
.card-img{position:relative;width:236px;height:168px}
.price{position:absolute;right:0;bottom:12px;background:var(--blue);color:#fff;font-size:13px;font-weight:700;padding:5px 10px}
.card-name{margin-top:12px;font-size:16px;font-weight:600;color:var(--heading)}
.card-text{font-size:12px;color:var(--grey);margin-top:3px}
.card-meta{font-size:11px;color:var(--grey);margin-top:2px}

/* sidebar */
.widget{width:215px;background:var(--panel)}
.widget-head{height:42px;background:var(--blue);color:#fff;font-size:13px;font-weight:600;display:flex;align-items:center;justify-content:center;letter-spacing:.5px}
.news-item{padding:14px 18px 0;font-size:11px;line-height:17px;color:var(--grey)}
.news-date{color:var(--blue);font-weight:600;display:block}
.read-more{margin:18px;font-size:11px;font-weight:700;color:var(--heading)}
.recent{padding:14px 18px 0}
.recent-img{width:179px;height:110px}
.recent-text{font-size:11px;line-height:16px;color:var(--grey);margin-top:8px}
.recent-text b{color:var(--blue)}

.divider{left:100px;top:1720px;width:1000px;height:1px;background:var(--grey-light)}

/* footer */
.footer{left:0;top:2090px;width:1200px;height:270px;background:var(--footer)}
.f-col{top:2130px;width:220px}
.f-title{color:#fff;font-size:12px;font-weight:600;letter-spacing:.5px;margin-bottom:16px}
.f-text{color:#9d9d9d;font-size:11px;line-height:18px}
.f-input{height:30px;border:1px solid #555;background:#3a3a3a;color:#888;font-size:11px;display:flex;align-items:center;padding:0 10px;margin-bottom:10px}
.f-btn{width:80px;height:30px;background:var(--blue);color:#fff;font-size:11px;font-weight:700;display:flex;align-items:center;justify-content:center}
.socials{display:flex;gap:12px;margin-top:14px}
.socials span{width:12px;height:12px;border-radius:50%;background:#888}
.bottom-bar{left:0;top:2360px;width:1200px;height:32px;background:var(--footer-bottom);color:#888;font-size:11px;display:flex;align-items:center;justify-content:center}
</style>
</head>
<body>
<div class="page">

  <div class="abs hero" role="img" aria-label="Coastal lighthouse on a rocky shore under a pastel evening sky"></div>
  <header class="abs nav">
    <div class="brand"><span class="brand-dot"></span><span>QWRB<br>Holdings</span></div>
    <ul class="menu">
      <li>HOME</li><li>ABOUT US</li><li>PROPERTIES</li><li>BLOG NEWS</li><li>CONTACT US</li><li class="login">LOGIN</li>
    </ul>
  </header>
  <h1 class="abs hero-title">QWRB HOLDINGS</h1>
  <div class="abs hero-btn">RENT YOUR HOME</div>
  <div class="abs slide-arrow" style="left:0"><svg width="12" height="18"><path d="M10 2 3 9l7 7" stroke="#fff" stroke-width="2.5" fill="none"/></svg></div>
  <div class="abs slide-arrow" style="right:0"><svg width="12" height="18"><path d="M2 2l7 7-7 7" stroke="#fff" stroke-width="2.5" fill="none"/></svg></div>

  <form class="abs search">
    <div class="field">Enter Keywords</div>
    <div class="search-row">
      <div class="search-col"><label>Property Type</label><div class="field">Any</div></div>
      <div class="search-col"><label>Location</label><div class="field">Any</div></div>
      <div class="search-col"><label>Select Status</label><div class="field">Any</div></div>
      <div class="search-col"><label>Price</label><div class="field">Min Price</div></div>
      <div class="search-col"><label>Bed</label><div class="field">Any</div></div>
      <div class="search-col"><label>Baths</label><div class="field">Any</div></div>
      <div class="search-btn">SEARCH</div>
    </div>
  </form>

  <section class="abs" style="left:100px;top:860px;width:740px">
    <h2 class="h2">Welcome to <span class="accent">QWRB</span> Holdings</h2>
    <p class="para" style="margin-top:18px">Sed ut perspiciatis unde omnis iste natus error sit voluptatem accusantium doloremque laudantium, totam rem aperiam, eaque ipsa quae ab illo inventore veritatis et quasi architecto beatae vitae dicta sunt explicabo. Nemo enim ipsam voluptatem quia voluptas sit aspernatur aut odit aut fugit, sed quia consequuntur magni dolores eos qui ratione voluptatem sequi nesciunt. Neque porro quisquam est, qui dolorem ipsum quia dolor sit amet, consectetur, adipisci velit.</p>
  </section>

  <h2 class="abs h2" style="left:100px;top:1080px">Latest Properties</h2>

  <div class="abs card" style="left:100px;top:1145px">
    <div class="card-img" role="img" aria-label="Photo of a two-storey family house with lawn" style="background:linear-gradient(180deg,#8fb6d8,#7a8f6a)"><span class="price">$230,000</span></div>
    <div class="card-name">Properties Name</div><div class="card-text">Lorem ipsum dolor - consectetur</div><div class="card-meta">Bed 3 | Bath 2 | 1,200 sqft</div>
  </div>
  <div class="abs card" style="left:352px;top:1145px">
    <div class="card-img" role="img" aria-label="Photo of a modern house at dusk" style="background:linear-gradient(180deg,#6a6f8e,#b89a7e)"><span class="price">$185,000</span></div>
    <div class="card-name">Properties Name</div><div class="card-text">Lorem ipsum dolor - consectetur</div><div class="card-meta">Bed 2 | Bath 1 | 950 sqft</div>
  </div>
  <div class="abs card" style="left:604px;top:1145px">
    <div class="card-img" role="img" aria-label="Photo of a couple in front of their new home" style="background:linear-gradient(180deg,#cfd8e2,#8a97a8)"><span class="price">$310,000</span></div>
    <div class="card-name">Properties Name</div><div class="card-text">Lorem ipsum dolor - consectetur</div><div class="card-meta">Bed 4 | Bath 2 | 1,800 sqft</div>
  </div>
  <div class="abs card" style="left:100px;top:1440px">
    <div class="card-img" role="img" aria-label="Photo of a house with a covered front porch" style="background:linear-gradient(180deg,#a8c2d8,#6f7d62)"><span class="price">$275,000</span></div>
    <div class="card-name">Properties Name</div><div class="card-text">Lorem ipsum dolor - consectetur</div><div class="card-meta">Bed 3 | Bath 2 | 1,400 sqft</div>
  </div>
  <div class="abs card" style="left:352px;top:1440px">
    <div class="card-img" role="img" aria-label="Photo of a house with a backyard pool" style="background:linear-gradient(180deg,#9fc4de,#4fa6c4)"><span class="price">$420,000</span></div>
    <div class="card-name">Properties Name</div><div class="card-text">Lorem ipsum dolor - consectetur</div><div class="card-meta">Bed 5 | Bath 3 | 2,600 sqft</div>
  </div>
  <div class="abs card" style="left:604px;top:1440px">
    <div class="card-img" role="img" aria-label="Photo of a large lit house at twilight" style="background:linear-gradient(180deg,#6d7fa0,#c9a97a)"><span class="price">$360,000</span></div>
    <div class="card-name">Properties Name</div><div class="card-text">Lorem ipsum dolor - consectetur</div><div class="card-meta">Bed 4 | Bath 3 | 2,100 sqft</div>
  </div>

  <aside class="abs widget" style="left:885px;top:870px;height:330px">
    <div class="widget-head">OUR NEWS</div>
    <div class="news-item">Sed ut perspiciatis unde omnis iste natus error sit voluptatem<span class="news-date">Feb 21, 2015</span></div>
    <div class="news-item">Sed ut perspiciatis unde omnis iste natus error sit voluptatem<span class="news-date">Feb 14, 2015</span></div>
    <div class="news-item">Sed ut perspiciatis unde omnis iste natus error sit voluptatem<span class="news-date">Feb 02, 2015</span></div>
    <div class="read-more">READ MORE</div>
  </aside>
  <aside class="abs widget" style="left:885px;top:1240px;height:460px">
    <div class="widget-head">RECENT PROPERTIES</div>
    <div class="recent">
      <div class="recent-img" role="img" aria-label="Photo of a suburban family house" style="background:linear-gradient(180deg,#9dbcd6,#6f8a5e)"></div>
      <div class="recent-text">Sed ut perspiciatis unde omnis iste natus<br><b>$230,000</b></div>
    </div>
    <div class="recent">
      <div class="recent-img" role="img" aria-label="Photo of a modern house at night" style="background:linear-gradient(180deg,#4e5d7e,#c59b6a)"></div>
      <div class="recent-text">Sed ut perspiciatis unde omnis iste natus<br><b>$310,000</b></div>
    </div>
  </aside>

  <div class="abs divider"></div>

  <h2 class="abs h2" style="left:100px;top:1815px;font-size:26px">New Haven Community</h2>
  <div class="abs" role="img" aria-label="Photo of a house on a tree-lined street" style="left:100px;top:1870px;width:145px;height:140px;background:linear-gradient(180deg,#a9c3d6,#6c7f5c)"></div>
  <p class="abs para" style="left:262px;top:1868px;width:230px;font-size:11px;line-height:18px">Sed ut perspiciatis unde omnis iste natus error sit voluptatem accusantium doloremque laudantium totam rem aperiam eaque ipsa.<br><br>Quae ab illo inventore veritatis et quasi architecto beatae vitae dicta.</p>

  <h2 class="abs h2" style="left:640px;top:1815px;font-size:26px">Renting Market</h2>
  <div class="abs" role="img" aria-label="Photo of a large house lit at dusk" style="left:640px;top:1870px;width:160px;height:140px;background:linear-gradient(180deg,#5e6f92,#caa06e)"></div>
  <p class="abs para" style="left:818px;top:1868px;width:270px;font-size:11px;line-height:18px">Sed ut perspiciatis unde omnis iste natus error sit voluptatem accusantium doloremque laudantium totam rem aperiam eaque ipsa.<br><br>Quae ab illo inventore veritatis et quasi architecto beatae vitae dicta.</p>

  <footer class="abs footer"></footer>
  <div class="abs f-col" style="left:100px">
    <div class="f-title">QWRB HOLDINGS ADDRESS</div>
    <p class="f-text">Sed ut perspiciatis unde omnis iste natus error sit voluptatem accusantium doloremque laudantium totam rem.</p>
    <p class="f-text" style="margin-top:14px;color:#ccc">Call Us: +1 (203) 555 0148<br>+1 (203) 555 0192</p>
    <div class="socials"><span></span><span></span><span></span><span></span><span></span></div>
  </div>
  <div class="abs f-col" style="left:375px">
    <div class="f-title">SUBSCRIBE TO BLOG VIA EMAIL</div>
    <p class="f-text" style="margin-bottom:12px">Enter your email address to subscribe to this blog and receive notifications.</p>
    <div class="f-input">Email Address</div>
    <div class="f-btn">SUBSCRIBE</div>
  </div>
  <div class="abs f-col" style="left:650px">
    <div class="f-title">RECENT COMMENTS</div>
    <p class="f-text">Jorge Martin on Lorem ipsum dolor<br>Lisa Bowen on Sed ut perspiciatis<br>Karen Holt on Nemo enim ipsam<br>Peter Vance on Neque porro quis<br>Jorge Martin on Totam rem aperiam</p>
  </div>
  <div class="abs f-col" style="left:925px;width:175px">
    <div class="f-title">LOGIN HERE</div>
    <div class="f-input">Username</div>
    <div class="f-input">Password</div>
    <div class="f-btn">LOGIN</div>
  </div>
  <div class="abs bottom-bar">Copyright © 2015 QWRB Holdings</div>

</div>
</body>
</html>
```